Seriöser Briefkopf für Rechtsanwaltskanzlei
Zielgruppe
Rechtsanwaltskanzlei
Aufgabenstellung
Benötigt wird ein seriöser Briefkopf für eine Anwaltskanzlei. Er soll im Wesentlichen aus Typen bestehen, mit denen aber durchaus 'gespielt' werden soll (Groß- und Kleinschreibung, querstehend, angeschnitten o.Ä)
Folgender Inhalt muss untergebracht werden:
Rechtsanwaltskanzlei Kessenhagen
Rechtsanwalt Dipl.-Ing. Udo Kessenhagen
Rechtsanwalt Matthias Wendel
Der Briefkopf muss schwarz-weiß druckbar sein und beim Versenden per Fax müssen alle Daten gut lesbar bleiben (also keine Grautöne bei Tel-Nr. o.Ä.)
Der Briefkopf soll mit einem Drucker ausgedruckt werden, sodass keine Gestaltung bis zum Blattrand gehen darf.
Bitte keine Logos mit Paragrafen-Zeichen oder Justitia und nicht die Abkürzung RUK verwenden.
Keine - Einfach drauflos - Ich bin gespannt

```html
<!DOCTYPE html>
<html lang="de">
<head>
<meta charset="utf-8">
<title>Briefbogen Rechtsanwaltskanzlei Kessenhagen</title>
<link rel="stylesheet" href="https://fonts.googleapis.com/css2?family=Open+Sans:wght@300;400&family=Arimo:wght@400&display=swap">
<style>
  :root{
    --bg:#b9bcbd;
    --paper:#f3f2f1;
    --ink:#1a1a1a;
    --soft:#6d6d6d;
    --accent:#d0202b;
  }
  *{margin:0;padding:0;box-sizing:border-box}
  html,body{width:1200px;height:919px;overflow:hidden;background:var(--bg)}
  .sheet{
    position:absolute;left:289px;top:20px;width:622px;height:880px;
    background:var(--paper);box-shadow:0 4px 18px rgba(0,0,0,.18);
    font-family:"Arimo",Arial,sans-serif;color:var(--ink);
  }
  .brand{position:absolute;left:70px;top:96px;font-family:"Open Sans",sans-serif;font-weight:300;color:var(--soft)}
  .brand-name{font-size:27px;letter-spacing:.5px;line-height:1}
  .brand-sub{font-size:9px;letter-spacing:1.6px;margin-top:3px;margin-left:64px}
  .seal{position:absolute;left:500px;top:28px}
  .contact{
    position:absolute;left:470px;top:80px;width:140px;
    font-family:"Open Sans",sans-serif;font-weight:400;font-size:7px;line-height:1.5;color:var(--ink);
  }
  .contact .label{font-size:5.5px;letter-spacing:.8px;text-transform:uppercase;margin-top:7px}
  .contact .role{font-size:6px;color:var(--ink)}
  .sender-line{position:absolute;left:44px;top:190px;font-family:"Open Sans",sans-serif;font-size:5.5px;color:var(--ink)}
  .recipient{position:absolute;left:44px;top:208px;font-size:10px;line-height:1.35}
  .letter{position:absolute;left:44px;top:290px;width:420px;font-size:9.6px;line-height:1.4}
  .letter p{margin-bottom:12px}
  .signature{margin-top:24px}
  .web{position:absolute;right:44px;bottom:40px;font-family:"Open Sans",sans-serif;font-size:8px;letter-spacing:1.2px;color:var(--soft);text-transform:uppercase}
</style>
</head>
<body>
<main class="sheet">
  <div class="brand">
    <div class="brand-name">Udo Kessenhagen</div>
    <div class="brand-sub">RECHTSANWALTSKANZLEI</div>
  </div>

  <svg class="seal" width="36" height="36" viewBox="0 0 36 36" aria-hidden="true">
    <circle cx="18" cy="18" r="17" fill="var(--accent)"/>
  </svg>

  <aside class="contact">
    <div>Udo Kessenhagen</div>
    <div class="role">Rechtsanwalt Dipl.-Ing.</div>
    <div style="margin-top:5px">Matthias Wendel</div>
    <div class="role">Rechtsanwalt</div>
    <div class="label">Kanzlei</div>
    <div>Lindenallee 7</div>
    <div>04109 Leipzig</div>
    <div>Tel 0341 58213 0</div>
    <div>Fax 0341 58213 49</div>
    <div>mail@kessenhagen-kanzlei.de</div>
    <div>www.kessenhagen-kanzlei.de</div>
    <div class="label">Steuernummer</div>
    <div>123/456/78910</div>
    <div class="label">Bankverbindung</div>
    <div>Bank XYZ</div>
    <div>BLZ 123 145 000</div>
    <div>Konto 12345678</div>
  </aside>

  <div class="sender-line">Rechtsanwaltskanzlei Kessenhagen · Lindenallee 7 · 04109 Leipzig</div>

  <address class="recipient" style="font-style:normal">
    Herr<br>Robert Exempelmann<br>Musterweg 5<br>07743 Jena
  </address>

  <section class="letter">
    <p>Sehr geehrte Damen &amp; Herren,</p>
    <p>Velit nis nim ver ipsuscilis ad duismod exeraes eismolo rperiure delestio cortio core dolore dolobore facipisi.</p>
    <p>Um aliquip erat lamcomm olortie min velismolent ulla coreet vel dolore tem in heniel ulla corem dolor suscidulpis amet dolortio od ercilisuis ate ming eu faccums andreet wiscilit ero od do ea facinim accumsan ute dolorpero et ea alit illam iriustin ut num velisciduni lut wisis at ipit wis diationsenim del ip eui blan utput pratie modip euisi esecte dunt ex ex euis accum illaor sed mod dunt aliquat ionsecte dolortin et vel dit. Sum ipisl exercip sumsan henim diam velendiam dolorper in vendrer am, consectem vel dionulputpat dolenim quip-susto et nulla feui te do eugiam, consequate te mincin ex ex et, sit aulet, cor irilla facidunis euis aut eraesto del utpat. Ut aliquisi blam aliquam conummy nulputpatum illa conse tinit lore enis ea alit la alis nonsequis dolessi tet la alis nostrud magna at, seniatum dolessi.</p>
    <p>Volese digna core consed tet praesto od tat lore faci tatem qui blamcor ad tem eugait ver accum inciliquisi iriustrud esse tat la faccums andipsustrud dolessecte, con erosto odiam quam augue ex eriustisisis enisis nonsecte magnibh ea ad dolore enim velesto consequis nim, velis nisi ip eu faccummy nullan henit velenis nim vero conse endre dolortin henisci blaore dunt luptat. Ostrud magnit etue venim adigna commodo lorper inibh enim veros dolore magna feuismo dipisci duipit praesto od tie molorem vullan ullaor sequam, quam eugait ute modignim dolore magnibh enibalorpero odolor si.</p>
    <p>Dundaerro beatatquis sumquia cusdam re explis molorem percia voloribus. Mos dent is modigente es cus. Aribusam, non ressunt inci cum rernat ullaborit dio. Nam cus voluptatias etur? Ici as eror magnatur alicilliat oditas doles est quationse iunt aut ullic tem alis quatibus, sam, ut eos esequidus. Dundaerro beatatquis sumquia cusdam re explis molorem percia voloribus. Mos dent is modigente es cus. Aribusam, non ressunt inci cum rernat ullaborit dio. Nam cus voluptatias etur? Ici as eror magnatur alicilliat oditas doles est quationse iunt aut ullic tem alis quatibus, sam, ut eos esequidus. Dundaerro beatatquis sumquia cusdam re explis molorem percia voloribus. Mos dent is modigente es cus. Aribusam, non ressunt inci cum rernat ullaborit dio. Nam cus voluptatias etu.</p>
    <p class="signature">Mit freundlichen Grüßen,<br>Max Mustermann</p>
  </section>

  <div class="web">www.kessenhagen-kanzlei.de</div>
</main>
</body>
</html>
```